Re-design of an existing website

We are needing a redesign of http://www.corvane-pharmacy.com/. Same colour scheme and content. The design needs to be done using Zurb Foundation 5 with all SCSS included and setup accordingly.

Placeholder images may be used for now as photo's are in progress. Must be responsive and work on all device types.
Updates

PLEASE NOTE: The project manager is currently on holidays until the 6th of September, hopefully we will have a decision closer to this date but it may be a few days after.

Industry/Entity Type

Medical

Coding

Coded - Design and coding required

Number of Pages Required

3 page

Font styles to use
Sans Serif

Requirements
Must have
• Zurb Foundation 5

```html
<!DOCTYPE html>
<html lang="en">
<head>
<meta charset="utf-8">
<title>The Corvane Pharmacy – Oncology Services</title>
<link href="https://fonts.googleapis.com/css2?family=Open+Sans:wght@400;600;700&family=Oswald:wght@400;500&display=swap" rel="stylesheet">
<style>
:root{
  --blue:#1a8fd6;
  --blue-dark:#0f6fad;
  --navy:#1d3f66;
  --ink:#333;
  --muted:#777;
  --line:#e3e7ea;
  --dark:#1f1f1f;
  --dark-2:#2a2a2a;
  --white:#fff;
  --paper:#f7f8f9;
}
*{box-sizing:border-box;margin:0;padding:0}
html,body{width:1200px;height:2500px;overflow:hidden;background:var(--white);font-family:"Open Sans",Arial,sans-serif;color:var(--ink)}
.page{width:1200px;height:2500px;position:relative}
.wrap{width:1040px;margin:0 auto;position:relative}

/* header */
.site-header{height:96px;border-bottom:1px solid var(--line)}
.site-header .wrap{display:flex;align-items:center;height:96px;justify-content:space-between}
.brand{display:flex;flex-direction:column}
.brand-name{font-size:22px;font-weight:700;color:var(--navy)}
.brand-tag{font-size:11px;color:var(--blue);margin-top:2px}
.header-right{display:flex;flex-direction:column;align-items:flex-end;gap:10px}
.utility{display:flex;gap:14px;align-items:center;font-size:11px;color:var(--muted)}
.search{width:140px;height:22px;border:1px solid var(--line);border-radius:2px;padding:0 6px;display:flex;align-items:center;justify-content:space-between;font-size:10px;color:#aaa}
.nav{display:flex;font-size:11px;font-weight:600;text-transform:uppercase;color:var(--navy)}
.nav a{padding:8px 12px;text-decoration:none;color:inherit}
.nav a.active{background:var(--blue);color:var(--white)}

/* hero */
.hero{height:520px;position:relative;background:linear-gradient(120deg,#e9eef2 0%,#cfd9e2 45%,#f3f5f7 100%)}
.hero-tag{position:absolute;left:640px;top:330px;background:var(--blue);color:var(--white);font-family:"Oswald",sans-serif;font-size:30px;padding:10px 22px;letter-spacing:.5px}
.hero-note{position:absolute;left:905px;top:318px;width:215px;background:rgba(255,255,255,.92);font-size:11px;line-height:1.5;padding:12px 14px;color:var(--ink);font-style:italic}

/* intro */
.intro{text-align:center;padding:42px 0 30px}
.intro small{font-size:12px;letter-spacing:1.5px;color:var(--muted);text-transform:uppercase}
.intro h1{font-family:"Oswald",sans-serif;font-weight:400;font-size:44px;color:var(--blue);margin-top:6px}
.intro .rule{width:60px;height:2px;background:var(--blue);margin:14px auto 0}

/* services */
.services{display:flex;gap:40px;padding:10px 0 50px}
.services-main{flex:1}
.services-main h2{font-size:20px;color:var(--blue);font-weight:600;margin-bottom:16px}
.services-main p{font-size:13px;line-height:1.75;color:var(--muted);margin-bottom:14px}
.btn{display:inline-block;background:var(--blue);color:var(--white);font-size:12px;padding:8px 18px;border-radius:2px;text-decoration:none;margin-top:6px}
.side-tabs{width:300px;border:1px solid var(--line)}
.tab{padding:16px 18px;border-bottom:1px solid var(--line)}
.tab h3{font-size:13px;text-transform:uppercase;color:var(--navy);font-weight:600}
.tab p{font-size:11px;color:var(--muted);line-height:1.5;margin-top:4px}
.tab.active{background:var(--blue);position:relative}
.tab.active h3,.tab.active p{color:var(--white)}
.tab.active:before{content:"";position:absolute;left:-12px;top:22px;border:8px solid transparent;border-right:8px solid var(--blue);border-left:0;width:0}

/* brochures */
.brochures{height:620px;background:linear-gradient(180deg,#3a3a3a,#262626);color:var(--white);text-align:center;padding-top:56px}
.brochures h2{font-family:"Oswald",sans-serif;font-weight:400;font-size:56px;letter-spacing:2px}
.brochures h3{font-family:"Oswald",sans-serif;font-weight:400;font-size:28px;letter-spacing:1.5px;margin-top:4px}
.brochures .hint{font-size:12px;letter-spacing:2px;color:#bbb;margin-top:14px}
.cards{display:flex;gap:14px;justify-content:center;margin-top:44px}
.card{width:160px;background:var(--white);color:var(--ink);padding-bottom:14px}
.card .thumb{height:150px;background:linear-gradient(135deg,#dfe6ec,#b8c6d2)}
.card h4{font-size:14px;font-weight:600;margin:12px 0 8px;color:var(--navy)}
.card .dl{display:inline-block;background:var(--blue);color:var(--white);font-size:9px;padding:4px 10px;border-radius:2px;text-transform:uppercase}
.dots{margin-top:24px;display:flex;gap:6px;justify-content:center}
.dots i{width:8px;height:8px;border-radius:50%;background:#666}
.dots i.on{background:var(--blue)}

/* news & clients */
.lower{display:flex;gap:60px;padding:44px 0 30px}
.lower h2{font-family:"Oswald",sans-serif;font-weight:400;font-size:26px;color:var(--blue);margin-bottom:20px}
.news{flex:1}
.news-items{display:flex;gap:24px}
.news-item{flex:1;display:flex;gap:12px}
.date{width:44px;text-align:center;font-size:10px;color:var(--muted)}
.date b{display:block;background:var(--blue);color:var(--white);font-size:18px;padding:4px 0}
.news-item p{font-size:12px;line-height:1.55;color:var(--muted)}
.clients{flex:1}
.quote{background:var(--blue);color:var(--white);font-size:12px;line-height:1.6;padding:16px 18px;position:relative;font-style:italic}
.quote:after{content:"";position:absolute;left:26px;bottom:-10px;border:10px solid transparent;border-top-color:var(--blue);border-bottom:0}
.author{display:flex;align-items:center;gap:10px;margin-top:20px;font-size:11px;color:var(--muted)}
.avatar{width:34px;height:34px;background:#cfd6dc}
.author b{display:block;color:var(--navy);font-size:12px}

/* footer */
.site-footer{position:absolute;left:0;bottom:0;width:1200px;height:240px;background:var(--dark);color:#bbb}
.site-footer .wrap{display:flex;gap:50px;padding-top:46px}
.foot-brand .brand-name{color:var(--white)}
.foot-brand p{font-size:10px;color:#888;margin-top:16px;line-height:1.6}
.foot-links{display:flex;gap:40px;font-size:12px}
.foot-links ul{list-style:none}
.foot-links li{margin-bottom:8px}
.foot-links li:before{content:"› ";color:var(--blue)}
.map{width:170px;height:120px;background:linear-gradient(135deg,#d8dcd4,#bfc7c0)}
.contact{font-size:11px;line-height:1.7}
.contact b{color:var(--white)}
</style>
</head>
<body>
<div class="page">

<header class="site-header">
  <div class="wrap">
    <div class="brand">
      <span class="brand-name">The Corvane Pharmacy</span>
      <span class="brand-tag">"Specialised Services for Special Needs"</span>
    </div>
    <div class="header-right">
      <div class="utility">
        <span>
          <svg width="10" height="10" viewBox="0 0 10 10"><path d="M2 1l2 2-1 1.5c.8 1.5 1.5 2.2 3 3L7.5 6l2 2-1.5 1.5C4.5 9 1 5.5.5 1.5z" fill="#1a8fd6"/></svg>
          +61 (07) 3000 4821
        </span>
        <span class="search">Search
          <svg width="10" height="10" viewBox="0 0 10 10"><circle cx="4" cy="4" r="3" fill="none" stroke="#999" stroke-width="1.3"/><path d="M6.3 6.3L9 9" stroke="#999" stroke-width="1.3"/></svg>
        </span>
      </div>
      <nav class="nav">
        <a href="#">Community Pharmacy</a><a href="#">CPAP</a><a href="#">NBR</a><a href="#" class="active">Oncology Services</a><a href="#">Home Nursing</a><a href="#">Nutrition</a><a href="#">Compounding</a><a href="#">Surgical Supply</a>
      </nav>
    </div>
  </div>
</header>

<section class="hero" role="img" aria-label="Photo of pharmacists working with lab equipment">
  <div class="hero-tag">ONCOLOGY SERVICES</div>
  <div class="hero-note">The Corvane Pharmacy is proud to be Australia's first and only fully Australian owned TGA approved cytotoxic compounding facility.</div>
</section>

<section class="intro">
  <small>Welcome to Corvane Pharmacy</small>
  <h1>Our Specialized Services</h1>
  <div class="rule"></div>
</section>

<section class="wrap services">
  <div class="services-main">
    <h2>Oncology Practice / Chemotherapy Production</h2>
    <p>The Corvane Pharmacy is at the centre of oncology pharmacy practice. We are heavily involved in the preparation of chemotherapy (cytotoxic) drugs. These drugs are prepared to doctor's orders in a cytotoxic drug safety cabinet within our newly refurbished and expanded, state of the art clean room facility.</p>
    <p>The Corvane Pharmacy is proud to be Australia's first and only fully Australian owned TGA approved cytotoxic compounding facility.</p>
    <p>The Corvane Pharmacy pioneered the provision of oncology pharmacy services in the Queensland private sector. We are the leading private sector pharmacy in Queensland providing drug dose preparation services. Our main four oncology pharmacists have over 50 years of combined experience in oncology pharmacy practice.</p>
    <p>Our patient focused approach drives us to ensure that we continue to improve.</p>
    <a class="btn" href="#">Contact Us</a>
  </div>
  <aside class="side-tabs">
    <div class="tab active"><h3>Oncology Services</h3><p>We are highly involved in the preparation of chemotherapy (cytotoxic) drugs.</p></div>
    <div class="tab"><h3>Sleep Apnoea</h3><p>Sleep apnoea identification right through to treatment and ongoing disease management.</p></div>
    <div class="tab"><h3>Pharmaceutical Compounding</h3><p>Compounding involves the preparation of unique medicines for individual patients.</p></div>
    <div class="tab"><h3>Home Nursing</h3><p>The leading provider nursing care to patients in the comfort of their own home for over 30 years.</p></div>
  </aside>
</section>

<section class="brochures">
  <h2>IMPLEMENTING</h2>
  <h3>INNOVATIVE IDEAS FOR SCIENTIFIC PROJECTS</h3>
  <p class="hint">CLICK BELOW TO VIEW BROCHURES</p>
  <div class="cards">
    <div class="card"><div class="thumb" role="img" aria-label="Photo of a mother and baby"></div><h4>Mother &amp; Baby</h4><span class="dl">Download</span></div>
    <div class="card"><div class="thumb" role="img" aria-label="Photo of a sleep apnoea mask"></div><h4>Sleep Apnoea</h4><span class="dl">Download</span></div>
    <div class="card"><div class="thumb" role="img" aria-label="Photo of medicine compounding"></div><h4>Compounding</h4><span class="dl">Download</span></div>
    <div class="card"><div class="thumb" role="img" aria-label="Photo of specialised products"></div><h4>Specialised Products</h4><span class="dl">Download</span></div>
    <div class="card"><div class="thumb" role="img" aria-label="Photo of oncology lab work"></div><h4>Oncology</h4><span class="dl">Download</span></div>
    <div class="card"><div class="thumb" role="img" aria-label="Photo of medical equipment"></div><h4>Medical Equipment</h4><span class="dl">Download</span></div>
  </div>
  <div class="dots"><i class="on"></i><i></i><i></i></div>
</section>

<section class="wrap lower">
  <div class="news">
    <h2>Health News</h2>
    <div class="news-items">
      <div class="news-item"><div class="date"><b>12</b>Aug</div><p>Hospital team shares new guidance on childhood vaccines as winter clinics open across the region – Daily Courier</p></div>
      <div class="news-item"><div class="date"><b>11</b>Aug</div><p>Local health forum calls for wider access to cancer care services in regional towns – Northern Herald</p></div>
    </div>
    <div class="dots"><i class="on"></i><i></i></div>
  </div>
  <div class="clients">
    <h2>Clients Words</h2>
    <div class="quote">"The team at Corvane made every step of my treatment easier. Staff were friendly, caring and always ready to answer questions. I would recommend their services to anyone needing special care."</div>
    <div class="author"><div class="avatar"></div><div><b>Mara Ellison</b>Customer</div></div>
  </div>
</section>

<footer class="site-footer">
  <div class="wrap">
    <div class="foot-brand">
      <span class="brand-name">The Corvane Pharmacy</span>
      <p>"Specialised Services for Special Needs"<br>© Corvane Pharmacy. All rights reserved.</p>
    </div>
    <div class="foot-links">
      <ul><li>Community Pharmacy</li><li>CPAP</li><li>NBR</li><li>Oncology Services</li></ul>
      <ul><li>Home Nursing</li><li>Nutrition</li><li>Compounding</li><li>Surgical Supply</li></ul>
    </div>
    <div class="map" role="img" aria-label="Map showing the pharmacy location"></div>
    <div class="contact">
      <b>The Corvane Pharmacy</b><br>Level 1, Corvane Medical Centre<br>24 Harbour St, Eastvale QLD<br>Phone: +61 (07) 3000 4821<br>hello@corvane-pharmacy.com
    </div>
  </div>
</footer>

</div>
</body>
</html>
```